Willowmere Surgery Brochure Design

Willowmere Surgery (willowmeresurgery.example)

Is a comprehensive breast care center that focuses on caring for women with breast cancer and other breast pathologies. We need a promotional and marketing brochure, in a tri-fold format, to provide information about our office and describe the services that we offer.

Deliverable

* The brochure should be completed by August 24th
* We will need the necessary files to get the brochure printed (.ai, .indd, etc).

Target Market(s)

Primarily patients of age between 30+ and 70+. The brochure will also be placed in doctor's waiting room

Industry/Entity Type

Marketing

Requirements
Must have
• * Make use of the color scheme as the website (http://willowmeresurgery.example, http://willowmeresurgery.example/static/theme-fuchsia.png)
* Incorporate the following graphic elements:
* The company’s logo (provided as an attachment)
* At least one images from the homepage
* Photos of the primary doctor and her staff
* Map to show the office location and phone number
* Enclose a breast cancer self-exam card (http://willowmeresurgery.example/static/shower-card.jpg)
* A portion of the brochure must be detachable and serve as business cards that can be cut off (see attachment).
Nice to have
• Here is an example of a brochure that we like:

http://plakmarket.example/item/flexible-trifold-brochure/731284?WT.ac=search_item&WT.seg_1=search_item&WT.z_author=dembrovi

```html
<!DOCTYPE html>
<html lang="en">
<head>
<meta charset="utf-8">
<title>Willowmere Surgery – Brochure Inside Spread</title>
<link rel="stylesheet" href="https://fonts.googleapis.com/css2?family=Pinyon+Script&family=Raleway:wght@300;400&display=swap">
<style>
  :root {
    --magenta: #c5128a;
    --magenta-bar: #c83f95;
    --pink-text: #d4368f;
    --pink-script: #e59bbf;
    --ink: #3b3b3b;
    --cream: #f1e4ab;
    --white: #ffffff;
  }
  * { box-sizing: border-box; margin: 0; padding: 0; }
  html, body { width: 1200px; height: 927px; overflow: hidden; background: var(--white); }
  .spread {
    position: relative; width: 1200px; height: 927px; overflow: hidden;
    background: var(--white);
    font-family: "Raleway", "Helvetica Neue", Arial, sans-serif;
    color: var(--ink);
  }
  .top-band {
    position: absolute; left: 0; top: 0; width: 1200px; height: 100px;
    background: var(--magenta);
  }
  .top-rule {
    position: absolute; left: 0; top: 105px; width: 1200px;
    border-top: 1px dotted #d9a9c6;
  }
  .panel-title {
    position: absolute; top: 26px;
    font-family: "Pinyon Script", cursive;
    font-size: 56px; line-height: 1; color: var(--white);
    white-space: nowrap; transform: translateX(-50%);
  }
  .title-comprehensive { left: 205px; }
  .title-dedicated { left: 600px; }
  .title-experience { left: 1015px; }

  .leaf-wash {
    position: absolute; left: 0; top: 120px; width: 818px; height: 700px;
    background: radial-gradient(ellipse 50% 60% at 50% 40%, rgba(242,198,218,0.28), rgba(255,255,255,0) 70%);
  }
  .body-copy {
    position: absolute; font-size: 16.4px; line-height: 21.3px; font-weight: 400;
    letter-spacing: 0.35px;
  }
  .body-copy p + p { margin-top: 21.3px; }
  .copy-left { left: 32px; top: 155px; width: 352px; }
  .copy-left .narrow { width: 268px; }
  .copy-middle { left: 443px; top: 145px; width: 342px; }

  .tagline {
    position: absolute; left: 443px; top: 400px; width: 330px;
    color: var(--pink-text);
  }
  .tagline .lead { font-size: 16.4px; letter-spacing: 0.5px; display: block; }
  .tagline .script {
    font-family: "Pinyon Script", cursive; font-size: 46px; line-height: 36px;
    display: block; color: var(--pink-script); white-space: nowrap;
  }
  .tagline .tail { font-size: 16.4px; letter-spacing: 0.5px; display: block; text-align: right; }

  .flower {
    position: absolute; left: 182px; top: 490px; width: 636px; height: 394px;
    background: radial-gradient(ellipse 60% 75% at 55% 85%,
      rgba(234,179,201,0.95) 0%, rgba(238,196,213,0.75) 45%, rgba(255,255,255,0) 85%);
  }

  .photo {
    position: absolute; left: 818px; top: 107px; width: 382px; height: 285px;
    background: linear-gradient(180deg, #a9aaa5 0%, #8f8f8a 55%, #4a4644 100%);
  }
  .photo-rule {
    position: absolute; left: 818px; top: 392px; width: 382px;
    border-top: 2px dotted var(--pink-text);
  }
  .bio-panel {
    position: absolute; left: 818px; top: 394px; width: 382px; height: 533px;
    background: var(--cream);
  }
  .bio-copy {
    position: absolute; left: 852px; top: 418px; width: 314px;
    font-size: 16.4px; line-height: 21.3px; letter-spacing: 0.35px; text-align: center;
  }
  .ribbon {
    position: absolute; left: 1050px; top: 722px; width: 122px; height: 140px;
    background: linear-gradient(160deg, rgba(247,194,214,0.6) 0%, rgba(214,90,140,0.55) 100%);
  }

  .footer-bar {
    position: absolute; left: 0; top: 884px; width: 818px; height: 43px;
    background: var(--magenta-bar);
    display: flex; align-items: center; padding-left: 22px;
    color: var(--white); font-size: 17px; font-weight: 300; white-space: nowrap;
    letter-spacing: 0.3px;
  }
  .footer-bar .words { display: flex; margin-left: 8px; font-weight: 400; letter-spacing: 0.4px; }
  .footer-bar .words span { padding: 0 5px; }
  .footer-bar .words span + span { border-left: 1px dotted var(--white); }
</style>
</head>
<body>
<main class="spread">
  <div class="top-band"></div>
  <div class="top-rule"></div>
  <h2 class="panel-title title-comprehensive">Comprehensive</h2>
  <h2 class="panel-title title-dedicated">Dedicated</h2>
  <h2 class="panel-title title-experience">Experience</h2>

  <div class="leaf-wash" role="img" aria-label="Faint pink leaf shapes in the background"></div>

  <div class="flower" role="img" aria-label="Close-up photograph of a pink lotus flower with a yellow centre"></div>

  <section class="body-copy copy-left">
    <p>We provide a caring, intimate environment where your dignity and health come first. Conveniently, we are situated next to Marlow Hospital, in the Hollis Brandt Cancer Center. Any necessary diagnostic and treatment tools are at our fingertips.</p>
    <p>We understand your anxiety. We know that when you are told that you need to be evaluated more closely, you want answers as quickly as possible. We are here to help. Being dedicated to breast care, we have a wealth of up-to-date knowledge about the latest advances in treatment. Your doctor will listen to your concerns and work with you to make sure you understand your options.</p>
    <p class="narrow">Our knowledgeable staff will help alleviate your anxiety with timely appointments, education and compassion. We will make sure you have all the facts to make the best decisions about your care.</p>
  </section>

  <section class="body-copy copy-middle">
    <p>We are dedicated to bringing to you the most fresh and knowledgeable breast care, including all diagnostic studies and surgical techniques. Unified team approach – one that includes communication with your primary doctor, laboratory, radiology and ancillary services. Appropriate resources – including support groups, therapy, oncology, radiation oncology, cancer societies and more.</p>
  </section>

  <p class="tagline">
    <span class="lead">THIS IS</span>
    <span class="script">truly comprehensive</span>
    <span class="tail">BREAST CARE</span>
  </p>

  <div class="photo" role="img" aria-label="Photograph of the doctor and a staff member standing together"></div>
  <div class="photo-rule"></div>
  <div class="bio-panel"></div>
  <p class="bio-copy">Dr. Kestrova has focused her entire practice on breast surgery. Being fellowshiptrained in oncoplastic breast surgery, she intensely believes in guiding the patient through the entire experience. She is comfortable treating patients of all ages, from birth to the elderly. She strives to bring compassion and caring to everything she does. Dr. Kestrova is passionate about making sure that her patients get the best care, that they are well-informed, and treated with dignity and respect.</p>
  <div class="ribbon" role="img" aria-label="Pink awareness ribbon illustration"></div>

  <footer class="footer-bar">
    Deeply understanding that you need to heal
    <span class="words"><span>PHYSICALLY</span><span>EMOTIONALLY</span><span>SPIRITUALLY</span></span>
  </footer>
</main>
</body>
</html>
```